Upscale business cards needed for family business

We need professional business cards created for several family members. We are a family business holding company. We would like these relatively simple and straightforward, but also with a unique element to set them apart. Probably stick with neutral and simple colors - white, grey etc. We need space for the traditional elements, including name, title, address, email/phone number. And we will be creating several from this template so it needs to be template that is easy to switch information in and out of.

Industry/Entity Type

Business

Contact Information for Business Card

Please include the attached Dunmore Ventures logo.

Requirements
Must have
• The attached Dunmore Ventures logo.

```html
<!DOCTYPE html>
<html lang="en">
<head>
<meta charset="utf-8">
<title>Dunmore Ventures – Business Card</title>
<link rel="stylesheet" href="https://fonts.googleapis.com/css2?family=Cinzel:wght@600&family=Montserrat:wght@300;400&family=Cutive+Mono&display=swap">
<style>
  :root {
    --page-bg: #e9e7e4;
    --card-top: #d7d3cf;
    --card-white: #ffffff;
    --card-band: #958e8b;
    --name-box: #cdc8c5;
    --ink: #161616;
    --ink-soft: #6f6a67;
    --contact-text: #ffffff;
  }
  * { margin: 0; padding: 0; box-sizing: border-box; }
  html, body { width: 1200px; height: 799px; overflow: hidden; background: var(--page-bg); }
  .card {
    position: absolute; left: 75px; top: 100px;
    width: 1050px; height: 600px;
    background: var(--card-white);
    box-shadow: 0 10px 30px rgba(0,0,0,.18);
    overflow: hidden;
  }
  .card__top-strip { position: absolute; left: 0; top: 0; width: 100%; height: 90px; background: var(--card-top); }
  .card__band { position: absolute; left: 0; top: 300px; width: 100%; height: 300px; background: var(--card-band); }
  .brand {
    position: absolute; left: 48px; top: 150px;
    font-family: "Cinzel", Georgia, serif; font-weight: 600;
    font-size: 44px; letter-spacing: 1px; color: var(--ink);
  }
  .identity {
    position: absolute; left: 640px; top: 262px;
    width: 380px; height: 128px;
    background: var(--name-box); border-radius: 16px;
    padding: 24px 28px;
  }
  .identity__name {
    font-family: "Cinzel", Georgia, serif; font-weight: 600;
    font-size: 36px; color: var(--ink); line-height: 1.1; white-space: nowrap;
  }
  .identity__title {
    font-family: "Cutive Mono", "Courier New", monospace;
    font-size: 24px; letter-spacing: 2px; color: var(--ink-soft); margin-top: 6px;
  }
  .contact {
    position: absolute; display: flex; align-items: flex-start; gap: 16px;
    font-family: "Montserrat", Arial, sans-serif; font-weight: 300;
    font-size: 24px; line-height: 1.3; color: var(--contact-text);
  }
  .contact__icon { width: 26px; height: 26px; flex: none; margin-top: 2px; }
  .contact--address { left: 48px; top: 345px; }
  .contact--phone { left: 48px; top: 455px; }
  .contact--web { left: 470px; top: 455px; }
  .contact--email { left: 470px; top: 520px; }
</style>
</head>
<body>
  <div class="card">
    <div class="card__top-strip"></div>
    <div class="card__band"></div>

    <div class="brand">Dunmore Ventures</div>

    <div class="identity">
      <div class="identity__name">Name Surname</div>
      <div class="identity__title">Designation</div>
    </div>

    <div class="contact contact--address">
      <svg class="contact__icon" viewBox="0 0 26 26"><circle cx="13" cy="13" r="13" fill="#fff"/><path d="M13 6a5 5 0 0 0-5 5c0 4 5 9 5 9s5-5 5-9a5 5 0 0 0-5-5zm0 7a2 2 0 1 1 0-4 2 2 0 0 1 0 4z" fill="#958e8b"/></svg>
      <div>418B W. Alder Creek Rd.<br>Millbrook, TX. 77531</div>
    </div>

    <div class="contact contact--phone">
      <svg class="contact__icon" viewBox="0 0 26 26"><circle cx="13" cy="13" r="13" fill="#fff"/><path d="M9 7l2.5 0 1 3.5-1.6 1.2a8 8 0 0 0 3.4 3.4l1.2-1.6 3.5 1v2.5c0 .6-.5 1-1 1A11 11 0 0 1 8 8c0-.6.4-1 1-1z" fill="#958e8b"/></svg>
      <div>(512) 555 - 0143</div>
    </div>

    <div class="contact contact--web">
      <svg class="contact__icon" viewBox="0 0 26 26"><circle cx="13" cy="13" r="13" fill="#fff"/><circle cx="13" cy="13" r="7" fill="none" stroke="#958e8b" stroke-width="1.6"/><path d="M6 13h14M13 6c-3 4-3 10 0 14M13 6c3 4 3 10 0 14" fill="none" stroke="#958e8b" stroke-width="1.4"/></svg>
      <div>www.DunmoreVentures.co</div>
    </div>

    <div class="contact contact--email">
      <svg class="contact__icon" viewBox="0 0 26 26"><circle cx="13" cy="13" r="13" fill="#fff"/><rect x="6.5" y="8.5" width="13" height="9" rx="1" fill="none" stroke="#958e8b" stroke-width="1.6"/><path d="M6.5 9l6.5 5 6.5-5" fill="none" stroke="#958e8b" stroke-width="1.6"/></svg>
      <div>Elena@DunmoreVentures.co</div>
    </div>
  </div>
</body>
</html>
```